Brindle 48 Focus Wheel

We need a professional **framework wheel diagram** designed for our detection dog training manual.

Our business is **Brindle 48 Dog Training**, and this graphic represents our **Detection Training Model**.

Please use the **attached reference images** as a guide for the structure and layout of the wheel.

### What we need

1. **Full wheel graphic**

* Clean circular framework wheel
* Similar structure to the attached example
* Clear sections and text
* Professional training manual style
* Transparent background

2. **Individual segment pieces**

We also need the **inner sections broken into separate pieces** (like the second reference image).

This will allow us to place each section on different pages of the manual when explaining the concepts.

Each piece should look like a **slice of the wheel**.

### Style

The design should look:

• Professional
• Clean and modern
• Structured and easy to read
• Suitable for a training manual

Avoid cartoon styles or clipart.

### Colours

Please use our brand colour palette (see attached image):

* Dark navy blue
* Steel blue
* Light blue
* White
* Light grey
* Dark grey

### Files required

Final files must include:

* Vector files (AI or EPS)
* Transparent PNG
* High-resolution PDF

Please also provide **each segment exported individually**

```html
<!DOCTYPE html>
<html lang="en">
<head>
<meta charset="utf-8">
<title>Brindle 48 Focus Wheel</title>
<link rel="stylesheet" href="https://fonts.googleapis.com/css2?family=Barlow:ital,wght@0,600;0,700;1,800&family=Oswald:wght@600&display=swap">
<style>
  :root{
    --bg:#ffffff;
    --ring:#e4e7eb;
    --navy:#1f2d4d;
    --band:#f5f6f8;
    --ink:#1f2d4d;
    --dark-grey:#2f3439;
    --centre:#e2e4e7;
    --white:#ffffff;
  }
  html,body{margin:0;padding:0;overflow:hidden;background:var(--bg);}
  .canvas{width:1200px;height:1200px;position:relative;overflow:hidden;background:var(--bg);}
  .wheel{position:absolute;left:0;top:0;width:1200px;height:1200px;}
  .ring-title{font-family:"Oswald",sans-serif;font-weight:600;fill:var(--navy);font-size:44px;}
  .band-title{font-family:"Oswald",sans-serif;font-weight:600;fill:var(--navy);font-size:26px;}
  .area-label{font-family:"Barlow",sans-serif;font-weight:700;fill:var(--white);font-size:27px;}
  .slice-label{font-family:"Barlow",sans-serif;font-weight:700;font-size:18px;text-anchor:middle;}
  .slice-label.top{fill:var(--ink);}
  .slice-label.bottom{fill:var(--white);}
  .centre-label{font-family:"Barlow",sans-serif;font-style:italic;font-weight:800;font-size:22px;fill:var(--dark-grey);text-anchor:middle;}
  .divider{stroke:rgba(255,255,255,.5);stroke-width:1;}
  .brand{position:absolute;left:44px;top:35px;width:180px;height:180px;}
  .brand-name{font-family:"Barlow",sans-serif;font-weight:700;font-size:26px;fill:var(--dark-grey);text-anchor:middle;}
  .shadow{filter:drop-shadow(0 6px 8px rgba(0,0,0,.22));}
  .segment{filter:drop-shadow(0 2px 3px rgba(0,0,0,.15));}
</style>
</head>
<body>
<div class="canvas">

  <svg class="brand" viewBox="0 0 180 180" aria-label="Brindle 48">
    <circle cx="90" cy="90" r="78" fill="none" stroke="var(--dark-grey)" stroke-width="4"/>
    <text class="brand-name" x="90" y="99">Brindle 48</text>
  </svg>

  <svg class="wheel" viewBox="0 0 1200 1200" aria-label="Brindle 48 Focus Wheel">
    <defs>
      <linearGradient id="steel" x1="0" y1="0" x2="1" y2="0">
        <stop offset="0" stop-color="#4f78a3"/><stop offset="1" stop-color="#1f3763"/>
      </linearGradient>
      <linearGradient id="steelUp" x1="0" y1="1" x2="1" y2="0">
        <stop offset="0" stop-color="#4a74a0"/><stop offset="1" stop-color="#1e345e"/>
      </linearGradient>
      <linearGradient id="mist" x1="0" y1="0" x2="1" y2="0">
        <stop offset="0" stop-color="#9db7d0"/><stop offset=".7" stop-color="#88a6c4"/><stop offset="1" stop-color="#55779e"/>
      </linearGradient>
      <linearGradient id="mistSide" x1="0" y1="0" x2="1" y2="0">
        <stop offset="0" stop-color="#9bb4cd"/><stop offset="1" stop-color="#5a7aa0"/>
      </linearGradient>
      <linearGradient id="lightBlue" x1="0" y1="0" x2="1" y2="1">
        <stop offset="0" stop-color="#dce8f2"/><stop offset="1" stop-color="#b4cde2"/>
      </linearGradient>
      <linearGradient id="greySlice" x1="0" y1="0" x2="1" y2="1">
        <stop offset="0" stop-color="#9aa2ab"/><stop offset="1" stop-color="#737c86"/>
      </linearGradient>

      <path id="outerArc" d="M155,603 A448,448 0 0 1 1051,603"/>
      <path id="bandTop" d="M322,603 A281,281 0 0 1 884,603"/>
      <path id="bandBottom" d="M322,603 A281,281 0 0 0 884,603"/>

      <path id="arcDevelopment" d="M348.4,348.4 A360,360 0 0 1 603,243"/>
      <path id="arcDistractions" d="M603,243 A360,360 0 0 1 857.6,348.4"/>
      <path id="arcBehaviour" d="M857.6,348.4 A360,360 0 0 1 935.6,465.2"/>
      <path id="arcHandler" d="M935.6,465.2 A360,360 0 0 1 963,603"/>
      <path id="arcTarget" d="M857.6,857.6 A360,360 0 0 0 963,603"/>
      <path id="arcSearch" d="M603,963 A360,360 0 0 0 857.6,857.6"/>
      <path id="arcReinforcement" d="M348.4,857.6 A360,360 0 0 0 603,963"/>
      <path id="arcDeployment" d="M243,603 A360,360 0 0 0 348.4,857.6"/>
      <path id="arcIntegrity" d="M243,603 A360,360 0 0 1 348.4,348.4"/>
    </defs>

    <!-- operational capacity area ring -->
    <circle class="shadow" cx="603" cy="603" r="476" fill="var(--ring)"/>
    <text class="ring-title" dominant-baseline="central">
      <textPath href="#outerArc" startOffset="50%" text-anchor="middle" textLength="570" lengthAdjust="spacing">OPERATIONAL CAPACITY AREA</textPath>
    </text>

    <!-- outer areas -->
    <g class="outer-areas shadow">
      <path d="M306,306 A420,420 0 0 1 603,183 L603,302 A301,301 0 0 0 390.2,390.2 Z" fill="url(#mist)"/>
      <path d="M603,183 A420,420 0 0 1 900,306 L815.8,390.2 A301,301 0 0 0 603,302 Z" fill="url(#mist)"/>
      <path d="M900,306 A420,420 0 0 1 991,442.3 L881.1,487.8 A301,301 0 0 0 815.8,390.2 Z" fill="url(#mistSide)"/>
      <path d="M991,442.3 A420,420 0 0 1 1023,603 L904,603 A301,301 0 0 0 881.1,487.8 Z" fill="url(#mistSide)"/>
      <path d="M1023,603 A420,420 0 0 1 900,900 L815.8,815.8 A301,301 0 0 0 904,603 Z" fill="url(#mistSide)"/>
      <path d="M900,900 A420,420 0 0 1 603,1023 L603,904 A301,301 0 0 0 815.8,815.8 Z" fill="url(#steelUp)"/>
      <path d="M603,1023 A420,420 0 0 1 306,900 L390.2,815.8 A301,301 0 0 0 603,904 Z" fill="url(#steel)"/>
      <path d="M306,900 A420,420 0 0 1 183,603 L302,603 A301,301 0 0 0 390.2,815.8 Z" fill="url(#steel)"/>
      <path d="M183,603 A420,420 0 0 1 306,306 L390.2,390.2 A301,301 0 0 0 302,603 Z" fill="url(#steel)"/>
    </g>
    <g class="outer-dividers">
      <line class="divider" x1="306" y1="306" x2="390.2" y2="390.2"/>
      <line class="divider" x1="603" y1="183" x2="603" y2="302"/>
      <line class="divider" x1="900" y1="306" x2="815.8" y2="390.2"/>
      <line class="divider" x1="991" y1="442.3" x2="881.1" y2="487.8"/>
      <line class="divider" x1="1023" y1="603" x2="904" y2="603"/>
      <line class="divider" x1="900" y1="900" x2="815.8" y2="815.8"/>
      <line class="divider" x1="603" y1="1023" x2="603" y2="904"/>
      <line class="divider" x1="306" y1="900" x2="390.2" y2="815.8"/>
      <line class="divider" x1="183" y1="603" x2="302" y2="603"/>
    </g>

    <g class="area-labels">
      <text class="area-label" dominant-baseline="central"><textPath href="#arcDevelopment" startOffset="55%" text-anchor="middle">Development</textPath></text>
      <text class="area-label" dominant-baseline="central"><textPath href="#arcDistractions" startOffset="50%" text-anchor="middle">Distractions</textPath></text>
      <text class="area-label" dominant-baseline="central"><textPath href="#arcBehaviour" startOffset="50%" text-anchor="middle">Behaviour</textPath></text>
      <text class="area-label" dominant-baseline="central"><textPath href="#arcHandler" startOffset="50%" text-anchor="middle">Handler</textPath></text>
      <text class="area-label" dominant-baseline="central"><textPath href="#arcTarget" startOffset="50%" text-anchor="middle">Target Odour</textPath></text>
      <text class="area-label" dominant-baseline="central"><textPath href="#arcSearch" startOffset="50%" text-anchor="middle">Search Method</textPath></text>
      <text class="area-label" dominant-baseline="central"><textPath href="#arcReinforcement" startOffset="50%" text-anchor="middle">Reinforcement</textPath></text>
      <text class="area-label" dominant-baseline="central"><textPath href="#arcDeployment" startOffset="50%" text-anchor="middle">Deployment</textPath></text>
      <text class="area-label" dominant-baseline="central"><textPath href="#arcIntegrity" startOffset="60%" text-anchor="middle">Integrity</textPath></text>
    </g>

    <!-- foundations band -->
    <circle cx="603" cy="603" r="301" fill="var(--band)"/>
    <text class="band-title" dominant-baseline="central">
      <textPath href="#bandTop" startOffset="50%" text-anchor="middle" textLength="340" lengthAdjust="spacing">DOG FOUNDATIONS</textPath>
    </text>
    <text class="band-title" dominant-baseline="central">
      <textPath href="#bandBottom" startOffset="50%" text-anchor="middle" textLength="560" lengthAdjust="spacing">OPERATIONAL CAPACITY AREA</textPath>
    </text>

    <!-- inner segments, each a separate slice -->
    <g class="inner-segments">
      <g class="segment" id="segment-genetic-suitability" transform="translate(-3.8,-1.2)">
        <path d="M603,603 L342,603 A261,261 0 0 1 391.9,449.6 Z" fill="url(#lightBlue)"/>
        <text class="slice-label top" x="433" y="553"><tspan x="433">Genetic</tspan><tspan x="433" dy="19">Suitability</tspan></text>
      </g>
      <g class="segment" id="segment-health-wellbeing" transform="translate(-2.4,-3.2)">
        <path d="M603,603 L391.9,449.6 A261,261 0 0 1 522.3,354.8 Z" fill="url(#lightBlue)"/>
        <text class="slice-label top" x="489" y="439"><tspan x="489">Health &amp;</tspan><tspan x="489" dy="19">Physical</tspan><tspan x="489" dy="19">Wellbeing</tspan></text>
      </g>
      <g class="segment" id="segment-engagement-relationship" transform="translate(0,-4)">
        <path d="M603,603 L522.3,354.8 A261,261 0 0 1 683.7,354.8 Z" fill="url(#lightBlue)"/>
        <text class="slice-label top" x="603" y="394"><tspan x="603">Engagement</tspan><tspan x="603" dy="19">Relationship</tspan></text>
      </g>
      <g class="segment" id="segment-reward-value" transform="translate(2.4,-3.2)">
        <path d="M603,603 L683.7,354.8 A261,261 0 0 1 814.1,449.6 Z" fill="url(#lightBlue)"/>
        <text class="slice-label top" x="717" y="439"><tspan x="717">Reward</tspan><tspan x="717" dy="19">Value</tspan></text>
      </g>
      <g class="segment" id="segment-arousal-regulation" transform="translate(3.8,-1.2)">
        <path d="M603,603 L814.1,449.6 A261,261 0 0 1 864,603 Z" fill="url(#lightBlue)"/>
        <text class="slice-label top" x="773" y="553"><tspan x="773">Arousal</tspan><tspan x="773" dy="19">Regulation</tspan></text>
      </g>
      <g class="segment" id="segment-read-the-dog" transform="translate(3.7,1.5)">
        <path d="M603,603 L864,603 A261,261 0 0 1 787.6,787.6 Z" fill="url(#greySlice)"/>
        <text class="slice-label bottom" x="773" y="663"><tspan x="773">Read the</tspan><tspan x="773" dy="19">Dog</tspan></text>
      </g>
      <g class="segment" id="segment-minimal-involvement" transform="translate(1.5,3.7)">
        <path d="M603,603 L787.6,787.6 A261,261 0 0 1 603,864 Z" fill="url(#greySlice)"/>
        <text class="slice-label bottom" x="676" y="755"><tspan x="676">Minimal</tspan><tspan x="676" dy="19">Necessary</tspan><tspan x="676" dy="19">Involvement</tspan></text>
      </g>
      <g class="segment" id="segment-search-coverage" transform="translate(-1.5,3.7)">
        <path d="M603,603 L603,864 A261,261 0 0 1 418.4,787.6 Z" fill="url(#greySlice)"/>
        <text class="slice-label bottom" x="530" y="755"><tspan x="530">Search</tspan><tspan x="530" dy="19">Coverage</tspan></text>
      </g>
      <g class="segment" id="segment-dog-safety" transform="translate(-3.7,1.5)">
        <path d="M603,603 L418.4,787.6 A261,261 0 0 1 342,603 Z" fill="url(#greySlice)"/>
        <text class="slice-label bottom" x="433" y="663"><tspan x="433">Dog</tspan><tspan x="433" dy="19">Safety</tspan></text>
      </g>
    </g>

    <!-- centre -->
    <circle class="shadow" cx="603" cy="603" r="70" fill="var(--centre)"/>
    <text class="centre-label" x="603" y="598"><tspan x="603">Detection</tspan><tspan x="603" dy="23">capacities</tspan></text>
  </svg>
</div>
</body>
</html>
```